Quillfield HVAC WordPress website design

Design a new modern, clean, website for HVAC mechanical business that uses company logo/colors for branding and recognition. Files attached are just for band and color information. Here is a website design that appeals to me https://www.kestwellpartners.com/

A clear description of who we are and what we do

An easily-navigated site map

An easily-navigated site map for mobile devices

Easy-to-find contact information

Obvious call to action for service, installs or to schedule estimates

about us page

Provide a way for potential customers to contact us via text or email

provide a way that allows a customer to upload a picture to request a service call or quote.

I'm looking for the design to be completed in WordPress

Industry/Entity Type

HVAC Mechanical & Building Automation / Controls contractor

Coding

Coded - Design and coding required

Number of Pages Required

5+ page

Colors
0054AA
0677BA
7BADD7
CADEEF
E8F1F8

Requirements
Must have
• Design a new modern, clean, website for HVAC mechanical business that uses company logo/colors for branding and recognition. Files attached are just for band and color information. Here is a website design that appeals to me https://www.kestwellpartners.com/ A clear description of who we are and what we do An easily-navigated site map An easily-navigated site map for mobile devices Easy-to-find contact information Obvious call to action for service, installs or to schedule estimates about us page Provide a way for potential customers to contact us via text or email provide a way that allows a customer to upload a picture to request a service call or quote.
Nice to have

```html
<!DOCTYPE html>
<html lang="en">
<head>
<meta charset="utf-8">
<title>Quillfield HVAC – Heating and Air Conditioning Services</title>
<link href="https://fonts.googleapis.com/css2?family=Cinzel:wght@600;700;800&family=Poppins:wght@400;500;600;700&display=swap" rel="stylesheet">
<style>
:root{
  --navy:#073a7e;
  --navy-dark:#0d1733;
  --blue:#0054aa;
  --sky:#7badd7;
  --ice:#e8f1f8;
  --paper:#f4f4f4;
  --ink:#111;
  --muted:#666;
  --orange:#f0542b;
  --white:#fff;
}
*{margin:0;padding:0;box-sizing:border-box}
html,body{width:1200px;height:4135px;overflow:hidden}
body{position:relative;font-family:"Poppins",sans-serif;color:var(--ink);background:var(--white)}
.abs{position:absolute}
.serif{font-family:"Cinzel",serif}

/* header */
.site-header{left:0;top:0;width:1200px;height:109px;background:#000;z-index:5}
.brand{left:48px;top:26px;width:210px;height:104px;border-radius:50%;background:var(--white);border:5px solid var(--navy);display:flex;align-items:center;justify-content:center;z-index:6}
.brand span{font-family:"Poppins",sans-serif;font-weight:700;color:var(--navy);font-size:21px}
.topbar{left:318px;top:20px;display:flex;gap:46px;color:#fff;font-size:14px;align-items:center}
.topbar .item{display:flex;align-items:center;gap:8px}
.topbar .dot{width:16px;height:16px;border-radius:50%;background:var(--blue)}
.socials-top{display:flex;gap:10px}
.socials-top i{display:block;width:12px;height:12px;border-radius:50%;background:#fff}
.main-nav{left:316px;top:62px;display:flex;gap:38px;font-family:"Cinzel",serif;font-weight:700;color:#fff;font-size:18px}
.btn-quote-top{left:988px;top:50px;width:172px;height:44px;background:var(--navy);color:#fff;font-family:"Cinzel",serif;font-weight:700;font-size:19px;display:flex;align-items:center;justify-content:center}

/* hero */
.hero{left:0;top:109px;width:1200px;height:820px;overflow:hidden}
.hero-photo{position:absolute;inset:0;background:linear-gradient(160deg,#4a4f55 0%,#8b949c 40%,#5b6066 70%,#2f3337 100%)}
.hero-shade{position:absolute;inset:0;background:rgba(0,0,0,.35)}
.hero-curve{position:absolute;left:0;top:0}
.hero-title{left:0;top:240px;width:1200px;text-align:center;color:#fff;font-family:"Cinzel",serif;font-weight:700;font-size:58px;line-height:65px;z-index:2}
.hero-sub{left:0;top:441px;width:1200px;text-align:center;color:#fff;font-size:20px;line-height:24px;z-index:2}
.hero-btn{left:481px;top:570px;width:230px;height:56px;background:var(--navy);color:#fff;font-family:"Cinzel",serif;font-weight:700;font-size:24px;display:flex;align-items:center;justify-content:center;z-index:2}

.band-paper{left:0;top:929px;width:1200px;height:543px;background:var(--paper)}

/* feature cards */
.feature{width:224px;height:190px;background:#fff;border-radius:8px;box-shadow:0 3px 12px rgba(0,0,0,.08);text-align:center;z-index:3}
.feature svg{margin-top:22px}
.feature h3{font-family:"Cinzel",serif;font-size:15px;font-weight:700;margin-top:6px;color:#222}
.feature p{font-size:7px;color:#777;line-height:14px;margin-top:8px}
.feature .more{font-size:10px;font-weight:600;color:var(--navy);margin-top:16px;display:flex;justify-content:center;align-items:center;gap:6px}

/* about */
.about-photo{left:98px;top:1043px;width:375px;height:297px;border-radius:8px;background:linear-gradient(120deg,#6b2a22 0%,#8c5a44 35%,#3f5f9a 70%,#b89a82 100%)}
.badge{left:389px;top:1220px;width:160px;height:160px;border-radius:50%;background:var(--navy);color:#fff;text-align:center}
.badge b{display:block;font-family:"Cinzel",serif;font-size:60px;line-height:60px;margin-top:34px}
.badge small{font-family:"Cinzel",serif;font-size:12px;font-weight:600}
.tab{top:1040px;width:230px;height:59px;background:var(--navy);color:#fff;font-family:"Cinzel",serif;font-weight:700;font-size:20px;display:flex;align-items:center;justify-content:center}
.tab-notch{left:684px;top:1098px;width:0;height:0;border-left:14px solid transparent;border-right:14px solid transparent;border-top:18px solid var(--navy)}
.about-text{left:585px;top:1126px;width:420px;color:#777;font-size:13.5px;line-height:17px}
.about-text p+p{margin-top:10px}
.about-btn{left:586px;top:1303px;width:165px;height:42px;background:var(--navy);color:#fff;font-family:"Cinzel",serif;font-weight:700;font-size:14px;display:flex;align-items:center;justify-content:center}

/* services */
.section-title{left:0;top:1540px;width:1140px;text-align:center;font-family:"Cinzel",serif;font-weight:800;font-size:44px}
.tile{width:266px;height:249px;border-radius:8px;overflow:hidden}
.tile .img{position:absolute;inset:0}
.tile .overlay{position:absolute;inset:0;background:linear-gradient(180deg,rgba(0,0,0,0) 35%,rgba(0,0,0,.45) 100%)}
.tile h4{position:absolute;left:20px;bottom:30px;color:#fff;font-weight:500;font-size:29px;line-height:37px}
.tile .bar{position:absolute;left:20px;bottom:20px;width:140px;height:3px;background:var(--blue)}
.tile.active{background:var(--navy)}
.tile.active .frame{position:absolute;left:7px;top:7px;right:7px;bottom:7px;border:2px solid #fff;border-radius:4px}
.tile.active h4{top:14px;bottom:auto}
.tile.active .bar{top:92px;bottom:auto;background:#fff;width:134px}
.tile.active p{position:absolute;left:30px;top:108px;width:220px;color:#fff;font-size:13px;line-height:24px}
.tile.active .mini{position:absolute;left:30px;top:196px;width:98px;height:18px;background:var(--orange);color:#fff;font-size:7px;display:flex;align-items:center;justify-content:center}

/* area & form */
.area-band{left:0;top:2353px;width:1200px;height:528px;background:var(--navy)}
.area-title{left:82px;top:2465px;color:#fff;font-family:"Cinzel",serif;font-weight:700;font-size:32px}
.area-list{left:76px;top:2554px;display:grid;grid-template-columns:222px 200px;row-gap:20px;color:#fff;font-size:22px}
.area-list div{display:flex;align-items:center;gap:16px;height:36px}
.quote-form{left:672px;top:2451px;width:469px;height:489px;background:#fff;border-radius:14px;box-shadow:0 4px 14px rgba(0,0,0,.15)}
.field{left:36px;width:393px;height:42px;background:var(--paper);border-radius:3px;font-size:13px;color:#444;padding:14px 14px}
.field.msg{height:130px}
.form-btn{left:87px;top:424px;width:304px;height:38px;background:#1e5a95;color:#fff;border-radius:3px;font-family:"Cinzel",serif;font-weight:700;font-size:12px;display:flex;align-items:center;justify-content:center}
.van{left:13px;top:2833px;width:782px;height:313px;border-radius:40% 46% 20% 20%/50% 50% 18% 18%;background:linear-gradient(180deg,#eef0f3 0%,#d7dce2 45%,#1d4f8f 68%,#2a2a2a 100%)}

/* testimonials */
.review{top:3199px;width:287px;height:201px;background:#f7f7f7;border:1px solid #eee}
.stars{position:absolute;left:26px;top:16px;color:var(--navy);font-size:26px;letter-spacing:3px}
.review p{position:absolute;left:35px;top:64px;width:225px;font-size:11.5px;color:#666;line-height:19px}
.reviewer{position:absolute;left:32px;top:124px;display:flex;gap:8px;align-items:center}
.reviewer .av{width:44px;height:44px;border-radius:50%;background:linear-gradient(180deg,#2d8fc4,#1d5d7c)}
.reviewer b{display:block;font-size:12px;font-weight:600}
.reviewer small{font-size:7px;color:var(--navy);font-weight:600}

/* footer */
.footer-shape{left:0;top:3440px}
.footer-brand{left:490px;top:3455px;width:252px;height:128px;border-radius:50%;background:#fff;border:5px solid var(--navy);display:flex;align-items:center;justify-content:center}
.footer-brand span{font-weight:700;color:var(--navy);font-size:24px}
.fcol{top:3750px;color:#fff}
.fcol h5{font-size:17px;font-weight:500}
.fcol .rule{width:48px;height:3px;background:var(--blue);margin-top:14px}
.fcol .about{font-size:13.5px;line-height:26.5px;margin-top:30px;width:240px}
.fsocial{display:flex;gap:12px;margin-top:20px}
.fsocial i{display:block;width:38px;height:38px;border-radius:50%;background:var(--blue)}
.contact-row{display:flex;gap:20px;margin-top:22px}
.contact-row svg{flex:none;margin-top:2px}
.contact-row b{display:block;font-size:14px;font-weight:600}
.contact-row span{font-size:14px}
.links{margin-top:22px;width:250px}
.links div{display:flex;justify-content:space-between;font-size:13px;padding:10px 0 11px;border-bottom:1px solid rgba(255,255,255,.15)}
.hours{margin-top:12px}
.hours .row{display:flex;gap:20px;margin-top:16px}
.hours b{display:block;font-size:14px;font-weight:600}
.hours span{font-size:14px}
</style>
</head>
<body>

<header class="abs site-header">
  <div class="abs topbar">
    <div class="item"><i class="dot"></i>info@website.com</div>
    <div class="item"><i class="dot"></i>(123) 456 7890</div>
    <div class="socials-top"><i></i><i></i><i></i></div>
  </div>
  <nav class="abs main-nav"><span>HOME</span><span>ABOUT</span><span>SERVICES</span><span>PRODUCTS</span><span>FINANCING</span></nav>
  <div class="abs btn-quote-top">GET A QUOTE</div>
</header>
<div class="abs brand"><span>Quillfield HVAC</span></div>

<section class="abs hero">
  <div class="hero-photo" role="img" aria-label="Technician installing ductwork in a ceiling"></div>
  <div class="hero-shade"></div>
  <svg class="hero-curve" width="1200" height="820" viewBox="0 0 1200 820">
    <circle cx="540" cy="1330" r="760" fill="var(--navy)"/>
    <circle cx="560" cy="1340" r="715" fill="var(--paper)"/>
    <rect x="0" y="760" width="1200" height="60" fill="var(--paper)"/>
  </svg>
  <h1 class="abs hero-title">HEATING AND<br>AIR CONDITIONING<br>SERVICES</h1>
  <p class="abs hero-sub">Lorem ipsum dolor sit amet, consectetuer adipiscing elit.<br>Aenean commodo ligula eget dolor.<br>Aenean massa. Cum sociis natoque penatibus et<br>magnis dis parturient montes, nascetur ridiculus mus.</p>
  <div class="abs hero-btn">GET A QUOTE</div>
</section>
<div class="abs band-paper"></div>

<div class="abs feature" style="left:210px;top:730px">
  <svg width="56" height="50" viewBox="0 0 56 50" fill="none" stroke="var(--navy)" stroke-width="2"><rect x="4" y="14" width="30" height="26"/><path d="M10 14v26M16 14v26M22 14v26M28 14v26M34 22h8c6 0 6 10 0 10h-4"/><circle cx="44" cy="10" r="6"/></svg>
  <h3>Heating</h3>
  <p>LOREM IPSUM DOLOR SIT AMET,<br>CONSECTETUER ADIPISCING ELIT.</p>
  <div class="more">READ MORE <svg width="20" height="10"><path d="M0 5h16M12 1l5 4-5 4" stroke="var(--navy)" stroke-width="2" fill="none"/></svg></div>
</div>
<div class="abs feature" style="left:504px;top:730px">
  <svg width="56" height="50" viewBox="0 0 56 50" fill="none" stroke="var(--navy)" stroke-width="2"><rect x="4" y="6" width="48" height="22" rx="3"/><circle cx="22" cy="30" r="10"/><path d="M10 44c4-4 8 4 12 0M30 44c4-4 8 4 12 0"/></svg>
  <h3>Cooling</h3>
  <p>LOREM IPSUM DOLOR SIT AMET,<br>CONSECTETUER ADIPISCING ELIT.</p>
  <div class="more">READ MORE <svg width="20" height="10"><path d="M0 5h16M12 1l5 4-5 4" stroke="var(--navy)" stroke-width="2" fill="none"/></svg></div>
</div>
<div class="abs feature" style="left:799px;top:730px">
  <svg width="56" height="50" viewBox="0 0 56 50" fill="none" stroke="var(--navy)" stroke-width="2.5"><path d="M10 44L40 14M36 6l10 10M14 6l32 38M8 10l6-6"/></svg>
  <h3>Repairs</h3>
  <p>LOREM IPSUM DOLOR SIT AMET,<br>CONSECTETUER ADIPISCING ELIT.</p>
  <div class="more">READ MORE <svg width="20" height="10"><path d="M0 5h16M12 1l5 4-5 4" stroke="var(--navy)" stroke-width="2" fill="none"/></svg></div>
</div>

<div class="abs about-photo" role="img" aria-label="Technician in a blue cap working on a wall-mounted boiler"></div>
<div class="abs badge"><b>10+</b><small>Years of Experience</small></div>
<div class="abs tab" style="left:583px">WHO WE ARE</div>
<div class="abs tab-notch"></div>
<div class="abs tab" style="left:831px">WHAT WE DO</div>
<div class="abs about-text">
  <p>Lorem ipsum dolor sit amet, consectetuer adipiscing elit.<br>Aenean commodo ligula eget dolor.<br>Aenean massa. Cum sociis natoque penatibus et<br>magnis dis parturient montes, nascetur ridiculus mus.</p>
  <p>Lorem ipsum dolor sit amet, consectetuer adipiscing elit.<br>Aenean commodo ligula eget dolor.<br>Aenean massa. Cum sociis natoque penatibus et<br>magnis dis parturient montes, nascetur ridiculus mus.</p>
</div>
<div class="abs about-btn">Read More</div>

<h2 class="abs section-title">What Services We Offer</h2>

<div class="abs tile" style="left:120px;top:1658px"><div class="img" role="img" aria-label="Technician fitting gas pipework" style="background:linear-gradient(130deg,#7a5a40,#5d7a9a,#a33a2a)"></div><div class="overlay"></div><h4>Gas<br>Fitting</h4><i class="bar"></i></div>
<div class="abs tile active" style="left:451px;top:1658px"><div class="frame"></div><h4 style="left:30px">Pipe<br>Fitting</h4><i class="bar" style="left:30px"></i><p>Nulla commodo dolor massa, vel pellentesque nulla congue quis.</p><div class="mini">READ MORE</div></div>
<div class="abs tile" style="left:806px;top:1658px"><div class="img" role="img" aria-label="Technician installing an outdoor condenser unit" style="background:linear-gradient(130deg,#3a3a3a,#9a9a9a,#555)"></div><div class="overlay"></div><h4>New<br>Installs</h4><i class="bar"></i></div>
<div class="abs tile" style="left:120px;top:1977px"><div class="img" role="img" aria-label="Technician checking a commercial duct" style="background:linear-gradient(130deg,#6b6a55,#c9c2b4,#8a7a66)"></div><div class="overlay"></div><h4>Commercial<br>Services</h4><i class="bar"></i></div>
<div class="abs tile" style="left:451px;top:1977px"><div class="img" role="img" aria-label="Workers in hard hats on a building site" style="background:linear-gradient(130deg,#8a9aa8,#c35a2a,#4a6a3a)"></div><div class="overlay"></div><h4>Building<br>Automations</h4><i class="bar"></i></div>
<div class="abs tile" style="left:806px;top:1977px"><div class="img" role="img" aria-label="Rooftop HVAC units on a residential building" style="background:linear-gradient(180deg,#4a4a4a,#8c8c8c,#b0b0b0)"></div><div class="overlay"></div><h4>Residential<br>Services</h4><i class="bar"></i></div>

<section class="abs area-band"></section>
<h2 class="abs area-title">Services Area</h2>
<div class="abs area-list">
  <div><svg width="36" height="36" viewBox="0 0 36 36"><circle cx="18" cy="18" r="18" fill="#fff"/><path d="M18 9a6 6 0 0 0-6 6c0 5 6 12 6 12s6-7 6-12a6 6 0 0 0-6-6z" fill="var(--navy)"/><circle cx="18" cy="15" r="2.2" fill="#fff"/></svg>Area Name</div>
  <div><svg width="36" height="36" viewBox="0 0 36 36"><circle cx="18" cy="18" r="18" fill="#fff"/><path d="M18 9a6 6 0 0 0-6 6c0 5 6 12 6 12s6-7 6-12a6 6 0 0 0-6-6z" fill="var(--navy)"/><circle cx="18" cy="15" r="2.2" fill="#fff"/></svg>Area Name</div>
  <div><svg width="36" height="36" viewBox="0 0 36 36"><circle cx="18" cy="18" r="18" fill="#fff"/><path d="M18 9a6 6 0 0 0-6 6c0 5 6 12 6 12s6-7 6-12a6 6 0 0 0-6-6z" fill="var(--navy)"/><circle cx="18" cy="15" r="2.2" fill="#fff"/></svg>Area Name</div>
  <div><svg width="36" height="36" viewBox="0 0 36 36"><circle cx="18" cy="18" r="18" fill="#fff"/><path d="M18 9a6 6 0 0 0-6 6c0 5 6 12 6 12s6-7 6-12a6 6 0 0 0-6-6z" fill="var(--navy)"/><circle cx="18" cy="15" r="2.2" fill="#fff"/></svg>Area Name</div>
  <div><svg width="36" height="36" viewBox="0 0 36 36"><circle cx="18" cy="18" r="18" fill="#fff"/><path d="M18 9a6 6 0 0 0-6 6c0 5 6 12 6 12s6-7 6-12a6 6 0 0 0-6-6z" fill="var(--navy)"/><circle cx="18" cy="15" r="2.2" fill="#fff"/></svg>Area Name</div>
  <div><svg width="36" height="36" viewBox="0 0 36 36"><circle cx="18" cy="18" r="18" fill="#fff"/><path d="M18 9a6 6 0 0 0-6 6c0 5 6 12 6 12s6-7 6-12a6 6 0 0 0-6-6z" fill="var(--navy)"/><circle cx="18" cy="15" r="2.2" fill="#fff"/></svg>Area Name</div>
  <div><svg width="36" height="36" viewBox="0 0 36 36"><circle cx="18" cy="18" r="18" fill="#fff"/><path d="M18 9a6 6 0 0 0-6 6c0 5 6 12 6 12s6-7 6-12a6 6 0 0 0-6-6z" fill="var(--navy)"/><circle cx="18" cy="15" r="2.2" fill="#fff"/></svg>Area Name</div>
  <div><svg width="36" height="36" viewBox="0 0 36 36"><circle cx="18" cy="18" r="18" fill="#fff"/><path d="M18 9a6 6 0 0 0-6 6c0 5 6 12 6 12s6-7 6-12a6 6 0 0 0-6-6z" fill="var(--navy)"/><circle cx="18" cy="15" r="2.2" fill="#fff"/></svg>Area Name</div>
</div>

<form class="abs quote-form">
  <div class="abs field" style="top:40px">Name</div>
  <div class="abs field" style="top:98px">Email</div>
  <div class="abs field" style="top:154px">Phone</div>
  <div class="abs field" style="top:214px">Select Service</div>
  <div class="abs field msg" style="top:273px;left:42px;width:389px">Message</div>
  <div class="abs form-btn">REQUEST A QUOTE NOW</div>
</form>

<div class="abs van" role="img" aria-label="Branded company service van in white and blue livery"></div>

<div class="abs review" style="left:93px"><div class="stars">★★★★★</div><p>Interdum et malesuada fames ac ante ipsum primis in faucibus donec tempor nisi neque.</p><div class="reviewer"><i class="av" role="img" aria-label="Reviewer portrait"></i><div><b>Lena Marsh</b><small>MANAGER</small></div></div></div>
<div class="abs review" style="left:445px"><div class="stars">★★★★★</div><p>Interdum et malesuada fames ac ante ipsum primis in faucibus donec tempor nisi neque.</p><div class="reviewer"><i class="av" role="img" aria-label="Reviewer portrait"></i><div><b>Lena Marsh</b><small>MANAGER</small></div></div></div>
<div class="abs review" style="left:794px"><div class="stars">★★★★★</div><p>Interdum et malesuada fames ac ante ipsum primis in faucibus donec tempor nisi neque.</p><div class="reviewer"><i class="av" role="img" aria-label="Reviewer portrait"></i><div><b>Lena Marsh</b><small>MANAGER</small></div></div></div>

<svg class="abs footer-shape" width="1200" height="695" viewBox="0 0 1200 695">
  <path d="M0 300 Q0 130 600 90 Q1200 130 1200 300 V695 H0 Z" fill="var(--navy)"/>
  <path d="M6 330 Q20 170 600 128 Q1180 170 1194 330 V695 H6 Z" fill="var(--navy-dark)"/>
</svg>
<div class="abs footer-brand"><span>Quillfield HVAC</span></div>

<div class="abs fcol" style="left:66px">
  <h5>ABOUT US</h5><div class="rule"></div>
  <p class="about">We are an award winning plumbing company with over 20 years experience in the business. We provide a wide range of services for both residential and commercial clients.</p>
  <div class="fsocial"><i></i><i></i><i></i></div>
</div>
<div class="abs fcol" style="left:358px">
  <h5>CONTACT US</h5><div class="rule"></div>
  <div class="contact-row" style="margin-top:32px"><svg width="18" height="22" viewBox="0 0 18 22" fill="none" stroke="#888" stroke-width="1.5"><path d="M9 1a7 7 0 0 0-7 7c0 6 7 13 7 13s7-7 7-13a7 7 0 0 0-7-7z"/><circle cx="9" cy="8" r="2.5"/></svg><div><b>Address:</b><span>48 Harlow Street, Brookvale, NY</span></div></div>
  <div class="contact-row"><svg width="20" height="20" viewBox="0 0 20 20" fill="none" stroke="#888" stroke-width="1.5"><path d="M4 2l4 4-2 3c1 3 3 5 6 6l3-2 4 4-3 3C8 19 1 12 1 5z"/></svg><div><b>Phone:</b><span>+1123456789</span></div></div>
  <div class="contact-row"><svg width="18" height="22" viewBox="0 0 18 22" fill="none" stroke="#888" stroke-width="1.5"><rect x="3" y="1" width="12" height="20" rx="2"/><path d="M8 17h2"/></svg><div><b>Mobile:</b><span>+1123456789</span></div></div>
  <div class="contact-row"><svg width="20" height="16" viewBox="0 0 20 16" fill="none" stroke="#888" stroke-width="1.5"><rect x="1" y="1" width="18" height="14"/><path d="M1 1l9 8 9-8"/></svg><div><b>Email:</b><span>support@quillfieldhvac.com</span></div></div>
</div>
<div class="abs fcol" style="left:650px">
  <h5>QUICK LINKS</h5><div class="rule"></div>
  <div class="links"><div><span>About</span><span>›</span></div><div><span>Contact</span><span>›</span></div><div><span>News List</span><span>›</span></div><div><span>Services</span><span>›</span></div><div><span>Shop</span><span>›</span></div></div>
</div>
<div class="abs fcol" style="left:942px">
  <h5>OPENING HOURS</h5><div class="rule"></div>
  <div class="hours">
    <div class="row" style="margin-top:32px"><svg width="24" height="24" viewBox="0 0 24 24" fill="none" stroke="#888" stroke-width="1.5"><circle cx="12" cy="12" r="10"/><path d="M12 6v6h5"/></svg><div><b>Monday - Friday</b><span>8:00 AM - 5:00 PM</span></div></div>
    <div class="row"><svg width="24" height="24" viewBox="0 0 24 24" fill="none" stroke="#888" stroke-width="1.5"><circle cx="12" cy="12" r="10"/><path d="M12 6v6h5"/></svg><div><b>Saturday</b><span>9:00 AM - 4:00 PM</span></div></div>
    <div class="row"><svg width="24" height="24" viewBox="0 0 24 24" fill="none" stroke="#888" stroke-width="1.5"><circle cx="12" cy="12" r="10"/><path d="M12 6v6h5"/></svg><div><b>Sunday</b><span>CLOSED</span></div></div>
  </div>
</div>

</body>
</html>
```